Business Card Design Project

Our slogan is "WANDER BEYOND LIMITS" and we are after something creative and different to go with our company image.

Criteria:
The business card will not be a standard size but it must be small or big enough to fit in a wallet.
It will be double sided
It will have our colours and the design will be based around our logo (attached)
No fancy text just clean sharp easy to read. we have been using the stag sans book font type so this or similar type is preferable (we are not locked in a font type.

For more information about us, please visit out website at www.glimtrovale.com.au

Target Market(s)

outdoor and recreational industry/market

Industry/Entity Type

Business

Requirements
Must have
• Logo
Slogan
website
contact details (phone and email)
Name and Position
social media facebook and youtube

```html
<!DOCTYPE html>
<html lang="en">
<head>
<meta charset="utf-8">
<title>Glimtrovale Business Card</title>
<link href="https://fonts.googleapis.com/css2?family=Montserrat:wght@400;500&display=swap" rel="stylesheet">
<style>
  :root {
    --stage: #e4e4e4;
    --card-dark: #151515;
    --card-light: #fafafa;
    --brand-orange: #e8502a;
    --ink: #1c1c1c;
    --ink-soft: #3a3a3a;
    --on-dark: #ffffff;
    --social-blue: #3b5998;
    --social-red: #c4302b;
  }
  * { box-sizing: border-box; margin: 0; padding: 0; }
  html, body {
    width: 1200px; height: 900px; overflow: hidden;
    background: var(--stage);
    font-family: "Montserrat", Arial, sans-serif;
  }
  .canvas { position: relative; width: 1200px; height: 900px; }
  .card {
    position: absolute; left: 200px; width: 800px; height: 260px;
    box-shadow: 0 10px 24px rgba(0,0,0,0.22);
  }
  .card--front { top: 120px; background: var(--card-dark); }
  .card--back { top: 500px; background: var(--card-light); }

  /* Front */
  .front-logo {
    position: absolute; left: 0; right: 0; top: 34px;
    display: flex; flex-direction: column; align-items: center;
  }
  .brand-ring {
    width: 112px; height: 112px; border-radius: 50%;
    border: 4px solid var(--brand-orange);
  }
  .brand-name {
    margin-top: 16px; font-weight: 400; font-size: 30px;
    letter-spacing: 3px; color: var(--on-dark);
  }
  .slogan {
    margin-top: 6px; font-size: 10px; font-weight: 500;
    letter-spacing: 3px; color: var(--on-dark);
  }

  /* Back */
  .back-logo {
    position: absolute; left: 50px; top: 40px;
    display: flex; align-items: center; gap: 14px;
  }
  .back-logo .brand-ring { width: 118px; height: 118px; }
  .back-logo .brand-name {
    margin-top: 0; font-size: 15px; letter-spacing: 2px; color: var(--brand-orange);
  }
  .contact { position: absolute; left: 450px; top: 40px; color: var(--ink); }
  .person-name { font-size: 26px; font-weight: 400; letter-spacing: 1.5px; }
  .person-role { font-size: 17px; color: var(--ink-soft); margin-top: 2px; }
  .contact-list { margin-top: 22px; list-style: none; }
  .contact-list li { display: flex; font-size: 17px; line-height: 22px; }
  .contact-label { width: 26px; color: var(--brand-orange); }
  .website { margin-top: 14px; font-size: 18px; margin-left: -14px; }
  .social { display: flex; gap: 16px; margin-top: 14px; margin-left: -4px; }
  .social-square { width: 30px; height: 30px; border-radius: 3px; }
  .social-square--one { background: var(--social-blue); }
  .social-square--two { background: var(--social-red); }
</style>
</head>
<body>
<main class="canvas">
  <section class="card card--front" aria-label="Card front">
    <div class="front-logo">
      <div class="brand-ring"></div>
      <div class="brand-name">GLIMTROVALE</div>
      <div class="slogan">WANDER BEYOND LIMITS</div>
    </div>
  </section>

  <section class="card card--back" aria-label="Card back">
    <div class="back-logo">
      <div class="brand-ring"></div>
      <div class="brand-name">GLIMTROVALE</div>
    </div>
    <div class="contact">
      <div class="person-name">MAREN TOLLEFSEN</div>
      <div class="person-role">Director</div>
      <ul class="contact-list">
        <li><span class="contact-label">M</span>0491570156</li>
        <li><span class="contact-label">E</span>info@glimtrovale.com.au</li>
      </ul>
      <div class="website">www.glimtrovale.com.au</div>
      <div class="social">
        <span class="social-square social-square--one"></span>
        <span class="social-square social-square--two"></span>
      </div>
    </div>
  </section>
</main>
</body>
</html>
```